Classy, Elegant, Simple Business Card Design

Looking to have a classy, simple, and elegant design. Want a top notch designed business card. I really like the look of the new brivo credit card. I also like the design I attached. I am trying to reach 21-29 year old females for booking us for there wedding or event. We offer Disc Jockey Service, Photo Booth Rentals, and Uplighting .

Target Market(s)

21-28 year old females

Contact Information for Business Card

Has to have logo, website, email, and phone number

Font styles to use
Other font styles liked:
• open to font choice, modern, clean
Designer to choose
33a6d7
0791cd
0555a3
ffffff

Requirements
Must have
• Has to have logo, website, email, and phone number
Nice to have
• I really like the design of the new brivo credit card. I also included my logo and some designs I like
Should not have
• clutter or too much info

```html
<!DOCTYPE html>
<html lang="en">
<head>
<meta charset="utf-8">
<title>Tidewell Event Group – Business Card</title>
<link href="https://fonts.googleapis.com/css2?family=Roboto:wght@400;500;700&display=swap" rel="stylesheet">
<style>
  :root {
    --sky: #33a6d7;
    --azure: #0791cd;
    --navy: #0555a3;
    --white: #ffffff;
    --ink: #222222;
    --stage: #2b2b2b;
  }
  * { box-sizing: border-box; margin: 0; padding: 0; }
  html, body { width: 1200px; height: 1200px; overflow: hidden; }
  body {
    background: var(--stage);
    font-family: "Roboto", Arial, sans-serif;
    display: flex;
    flex-direction: column;
    align-items: center;
    justify-content: center;
    gap: 60px;
  }
  .card {
    position: relative;
    width: 840px;
    height: 480px;
    background: var(--white);
    border-radius: 36px;
  }
  .brand {
    position: absolute;
    display: flex;
    align-items: center;
    gap: 14px;
  }
  .brand-dot {
    width: 30px;
    height: 30px;
    border-radius: 50%;
    background: var(--azure);
  }
  .brand-name {
    font-size: 40px;
    font-weight: 500;
    color: var(--azure);
    letter-spacing: 1px;
  }
  .card-front .brand { top: 60px; right: 70px; }
  .card-back .brand { bottom: 70px; right: 70px; }

  .person { position: absolute; top: 110px; left: 70px; }
  .person-name { font-size: 30px; font-weight: 700; color: var(--azure); }
  .person-role { font-size: 18px; color: var(--ink); margin-top: 2px; }
  .person-email { font-size: 19px; color: var(--ink); margin-top: 34px; }

  .contact { position: absolute; bottom: 60px; left: 70px; }
  .contact-phone {
    display: flex;
    align-items: center;
    gap: 10px;
    font-size: 32px;
    font-weight: 700;
    color: #333333;
  }
  .contact-phone svg { width: 22px; height: 34px; }
  .contact-web { font-size: 19px; color: var(--navy); margin-top: 6px; margin-left: 32px; }
</style>
</head>
<body>
  <section class="card card-front">
    <div class="brand">
      <span class="brand-dot"></span>
      <span class="brand-name">Tidewell Event Group</span>
    </div>
    <div class="person">
      <p class="person-name">Marcus Hale</p>
      <p class="person-role">Founder</p>
      <p class="person-email">info@TidewellEvents.com</p>
    </div>
    <div class="contact">
      <p class="contact-phone">
        <svg viewBox="0 0 22 34" aria-hidden="true">
          <rect x="2" y="2" width="18" height="30" rx="3" fill="none" stroke="#33a6d7" stroke-width="2.5"/>
          <line x1="8" y1="27" x2="14" y2="27" stroke="#33a6d7" stroke-width="2"/>
        </svg>
        555-014-2290
      </p>
      <p class="contact-web">www.tidewellevents.com</p>
    </div>
  </section>

  <section class="card card-back">
    <div class="brand">
      <span class="brand-dot"></span>
      <span class="brand-name">Tidewell Event Group</span>
    </div>
  </section>
</body>
</html>
```